Brackwell HVAC Service LLC Business Card

We just got a design created by one of your designers for a logo and now would like help with a business card design. The information to be included on the card is as follows:
Brackwell HVAC Service LLC (I will attach logo design)
P.O. Box 418
Pinecrest, NE 69041
(308) 555-0147
Dale Vonnholt
I might include an e-mail address, but I'm not sure yet.
Target Market(s)
Customers needing service or repairs done on their heating and air conditioning systems.
Industry/Entity Type
Business
Contact Information for Business Card
P.O. Box 418
Pinecrest, NE 69041
(308) 555-0147
Dale Vonnholt

```html
<!DOCTYPE html>
<html lang="en">
<head>
<meta charset="utf-8">
<title>Brackwell HVAC Service LLC – Business Card</title>
<link rel="stylesheet" href="https://fonts.googleapis.com/css2?family=Roboto:wght@500;700&family=Roboto+Condensed:wght@400;700&display=swap">
<style>
  :root {
    --backdrop: #e9e9eb;
    --card: #fbfbfb;
    --navy: #1d3a86;
    --red: #c8101b;
    --red-deep: #a80812;
    --white: #ffffff;
  }
  * { box-sizing: border-box; margin: 0; padding: 0; }
  html, body {
    width: 1200px; height: 972px; overflow: hidden;
    background: var(--backdrop);
  }
  .canvas {
    position: relative; width: 1200px; height: 972px;
    display: flex; align-items: center; justify-content: center;
  }
  .card {
    position: relative; width: 840px; height: 480px;
    background: var(--card);
    box-shadow: 0 10px 30px rgba(0,0,0,0.12);
    overflow: hidden;
  }
  .brand {
    position: absolute; left: 410px; top: 84px;
    display: flex; align-items: center; gap: 18px;
  }
  .brand-dot {
    width: 70px; height: 70px; border-radius: 50%;
    background: var(--navy); flex: none;
  }
  .brand-name {
    font-family: "Roboto Condensed", sans-serif;
    font-weight: 700; font-size: 32px; line-height: 1.1;
    color: var(--navy); letter-spacing: 1px; text-transform: uppercase;
  }
  .rule-top {
    position: absolute; left: 0; right: 0; top: 236px; height: 5px;
    background: var(--red);
  }
  .contact-band {
    position: absolute; left: 0; right: 0; top: 248px; height: 196px;
    background: var(--navy);
  }
  .contact-list {
    position: absolute; left: 470px; top: 26px;
    list-style: none;
    font-family: "Roboto Condensed", sans-serif;
    font-size: 24px; color: var(--white);
  }
  .contact-list li {
    display: flex; align-items: center; gap: 10px; height: 40px;
    white-space: nowrap;
  }
  .contact-list svg { width: 22px; height: 22px; flex: none; }
  .name-tab {
    position: absolute; left: 0; top: 340px;
    width: 330px; height: 70px;
    background: linear-gradient(180deg, var(--red) 0%, var(--red-deep) 100%);
    border-radius: 0 14px 14px 0;
    display: flex; align-items: center; padding-left: 70px;
    font-family: "Roboto", sans-serif; font-weight: 500;
    font-size: 31px; color: var(--white); white-space: nowrap;
  }
</style>
</head>
<body>
<main class="canvas">
  <article class="card">
    <header class="brand">
      <span class="brand-dot"></span>
      <span class="brand-name">Brackwell HVAC<br>Service LLC</span>
    </header>

    <div class="rule-top"></div>

    <section class="contact-band">
      <ul class="contact-list">
        <li>
          <svg viewBox="0 0 24 24" aria-hidden="true"><circle cx="12" cy="12" r="11" fill="#fff"/><path d="M12 5a4.5 4.5 0 0 0-4.5 4.5C7.5 13 12 18.5 12 18.5s4.5-5.5 4.5-9A4.5 4.5 0 0 0 12 5zm0 6.3a1.8 1.8 0 1 1 0-3.6 1.8 1.8 0 0 1 0 3.6z" fill="#1d3a86"/></svg>
          <span>P.O. Box 418, Pinecrest, NE 69041</span>
        </li>
        <li>
          <svg viewBox="0 0 24 24" aria-hidden="true"><circle cx="12" cy="12" r="11" fill="#fff"/><path d="M8.6 6.5l1.8-.3 1.1 2.8-1.3 1a7.5 7.5 0 0 0 3.6 3.6l1-1.3 2.8 1.1-.3 1.8c-.2.9-1 1.4-1.9 1.3A10.5 10.5 0 0 1 7.3 8.4c-.1-.9.4-1.7 1.3-1.9z" fill="#1d3a86"/></svg>
          <span>(308) 555-0147</span>
        </li>
        <li>
          <svg viewBox="0 0 24 24" aria-hidden="true"><circle cx="12" cy="12" r="10" fill="none" stroke="#fff" stroke-width="1.6"/><rect x="6.5" y="8" width="11" height="8" fill="none" stroke="#fff" stroke-width="1.4"/><path d="M6.5 8l5.5 4.5L17.5 8" fill="none" stroke="#fff" stroke-width="1.4"/></svg>
          <span>dale@brackwellhvac.com</span>
        </li>
      </ul>
    </section>

    <div class="name-tab">Dale Vonnholt</div>
  </article>
</main>
</body>
</html>
```